Closed loop end of life cycle for electronics Loop.

Sustainability Closed Loop. I need six sections on the Closed Loop
1-End-of-life Product & Mfg. Scrap
2-UBNE Services
3-Mechanical Processing
4-Precious Metals Refining
5-Metal Products Manufactured
6-Products return to OEMs
Target Market(s)
Vorex, Norby, KGWR, other major manufacturers of electronics and semiconductor
Industry/Entity Type
Sustainablek
Font styles to use
Serif
Sans Serif
Colors
0054AA
0677BA
7BADD7
CADEEF
E8F1F8
0094D4
00A9DD
6FCCEA
C7EBF8
E9F6FB
00AB8E
00BBA5
67D7C9
C6EFE9
E9F9F6
Requirements
Must have
- Sustainability Closed Loop. I need six sections on the Closed Loop ring below.

```html
<!DOCTYPE html>
<html lang="en">
<head>
<meta charset="utf-8">
<title>ELM Sustainability &amp; Renewable Resource Loop</title>
<link rel="stylesheet" href="https://fonts.googleapis.com/css2?family=EB+Garamond:wght@400;700&display=swap">
<style>
  :root {
    --page: #ffffff;
    --ink: #111111;
    --label: #ffffff;
    --scrap: #1769b3;
    --ubne: #1388cd;
    --mech: #0b836a;
    --refine: #14b09a;
    --metal: #5fcfc2;
    --return: #0e4a8b;
    --scrap-lt: #5b9ccc;
    --ubne-lt: #5aaadb;
    --mech-lt: #55a99a;
    --refine-lt: #55c8b6;
    --metal-lt: #8edfd4;
    --return-lt: #5679a8;
  }
  html, body { margin: 0; padding: 0; overflow: hidden; background: var(--page); }
  .canvas { width: 1181px; height: 1200px; display: block; }
  .seg-label {
    font-family: "EB Garamond", Garamond, serif;
    font-size: 32px;
    fill: var(--label);
    text-anchor: middle;
  }
  .loop-title {
    font-family: "EB Garamond", Garamond, serif;
    font-weight: 700;
    font-size: 50px;
    fill: var(--ink);
    text-anchor: middle;
    letter-spacing: 1px;
  }
  .fill-scrap { fill: var(--scrap); }
  .fill-ubne { fill: var(--ubne); }
  .fill-mech { fill: var(--mech); }
  .fill-refine { fill: var(--refine); }
  .fill-metal { fill: var(--metal); }
  .fill-return { fill: var(--return); }
  .fill-scrap-lt { fill: var(--scrap-lt); }
  .fill-ubne-lt { fill: var(--ubne-lt); }
  .fill-mech-lt { fill: var(--mech-lt); }
  .fill-refine-lt { fill: var(--refine-lt); }
  .fill-metal-lt { fill: var(--metal-lt); }
  .fill-return-lt { fill: var(--return-lt); }
</style>
</head>
<body>
<svg class="canvas" viewBox="0 0 1904 1935" width="1181" height="1200" xmlns="http://www.w3.org/2000/svg">
  <defs>
    <path id="arrow" d="M -185 -320.4 A 370 370 0 0 1 126.5 -347.7 L 135.1 -371.2 L 150.2 -282.5 L 83.8 -230.2 L 92.3 -253.7 A 270 270 0 0 0 -135 -233.8 L -125 -294.6 Z"/>
    <path id="cw-outer" d="M 0 328 A 328 328 0 1 1 0 -328 A 328 328 0 1 1 0 328"/>
    <path id="cw-inner" d="M 0 288 A 288 288 0 1 1 0 -288 A 288 288 0 1 1 0 288"/>
    <path id="cw-mid" d="M 0 308 A 308 308 0 1 1 0 -308 A 308 308 0 1 1 0 308"/>
    <path id="ccw-inner" d="M 0 307 A 307 307 0 1 0 0 -307 A 307 307 0 1 0 0 307"/>
    <path id="ccw-outer" d="M 0 347 A 347 347 0 1 0 0 -347 A 347 347 0 1 0 0 347"/>
    <clipPath id="inner-band"><circle r="319"/></clipPath>
    <linearGradient id="grad-scrap" x1="0" y1="0" x2="1" y2="0"><stop offset="0" stop-color="#1664ae"/><stop offset="0.55" stop-color="#2a8fd6"/><stop offset="1" stop-color="#b4f3ff"/></linearGradient>
    <linearGradient id="grad-ubne" x1="0" y1="0" x2="1" y2="0"><stop offset="0" stop-color="#0f7cc4"/><stop offset="0.55" stop-color="#3a9ee0"/><stop offset="1" stop-color="#b8eeff"/></linearGradient>
    <linearGradient id="grad-mech" x1="0" y1="0" x2="1" y2="0"><stop offset="0" stop-color="#0b7f67"/><stop offset="0.5" stop-color="#249f88"/><stop offset="1" stop-color="#6fdcc7"/></linearGradient>
    <linearGradient id="grad-refine" x1="0" y1="0" x2="1" y2="0"><stop offset="0" stop-color="#0c9a80"/><stop offset="0.55" stop-color="#3cc2ad"/><stop offset="1" stop-color="#d0fff8"/></linearGradient>
    <linearGradient id="grad-metal" x1="0" y1="0" x2="1" y2="0"><stop offset="0" stop-color="#55c6b6"/><stop offset="0.5" stop-color="#72d6c8"/><stop offset="1" stop-color="#dcfff7"/></linearGradient>
    <linearGradient id="grad-return" x1="0" y1="0" x2="1" y2="0"><stop offset="0" stop-color="#0c3f7c"/><stop offset="0.5" stop-color="#2c6fb6"/><stop offset="1" stop-color="#8ed0ff"/></linearGradient>
  </defs>

  <!-- Ring A: gradient arrows -->
  <g class="loop loop-gradient" transform="translate(465 455)">
    <g transform="rotate(0)"><use href="#arrow" fill="url(#grad-scrap)"/>
      <text class="seg-label"><textPath href="#cw-outer" startOffset="49.6%">End-of-life Product</textPath></text>
      <text class="seg-label"><textPath href="#cw-inner" startOffset="49.6%">&amp; Mfg. Scrap</textPath></text></g>
    <g transform="rotate(60)"><use href="#arrow" fill="url(#grad-ubne)"/>
      <text class="seg-label"><textPath href="#cw-mid" startOffset="49.6%">UBNE Services</textPath></text></g>
    <g transform="rotate(120)"><use href="#arrow" fill="url(#grad-mech)"/>
      <text class="seg-label"><textPath href="#cw-outer" startOffset="49.6%">Mechanical</textPath></text>
      <text class="seg-label"><textPath href="#cw-inner" startOffset="49.6%">Processing</textPath></text></g>
    <g transform="rotate(180)"><use href="#arrow" fill="url(#grad-refine)"/>
      <text class="seg-label"><textPath href="#ccw-inner" startOffset="50.4%">Refining</textPath></text>
      <text class="seg-label"><textPath href="#ccw-outer" startOffset="50.4%">Precious Metals</textPath></text></g>
    <g transform="rotate(240)"><use href="#arrow" fill="url(#grad-metal)"/>
      <text class="seg-label"><textPath href="#cw-outer" startOffset="49.6%">Metal Products</textPath></text>
      <text class="seg-label"><textPath href="#cw-inner" startOffset="49.6%">Manufactured</textPath></text></g>
    <g transform="rotate(300)"><use href="#arrow" fill="url(#grad-return)"/>
      <text class="seg-label"><textPath href="#cw-outer" startOffset="49.6%">Products Return</textPath></text>
      <text class="seg-label"><textPath href="#cw-inner" startOffset="49.6%">to OEMs</textPath></text></g>
    <text class="loop-title" y="-150">ELM</text>
    <text class="loop-title" y="-77">SUSTAINABILITY</text>
    <text class="loop-title" y="-5">&amp; RENEWABLE</text>
    <text class="loop-title" y="65">RESOURCE</text>
    <text class="loop-title" y="137">LOOP</text>
  </g>

  <!-- Ring B: flat arrows -->
  <g class="loop loop-flat" transform="translate(1408 455)">
    <g transform="rotate(0)"><use href="#arrow" class="fill-scrap"/>
      <text class="seg-label"><textPath href="#cw-outer" startOffset="49.6%">End-of-life Product</textPath></text>
      <text class="seg-label"><textPath href="#cw-inner" startOffset="49.6%">&amp; Mfg. Scrap</textPath></text></g>
    <g transform="rotate(60)"><use href="#arrow" class="fill-ubne"/>
      <text class="seg-label"><textPath href="#cw-mid" startOffset="49.6%">UBNE Services</textPath></text></g>
    <g transform="rotate(120)"><use href="#arrow" class="fill-mech"/>
      <text class="seg-label"><textPath href="#cw-outer" startOffset="49.6%">Mechanical</textPath></text>
      <text class="seg-label"><textPath href="#cw-inner" startOffset="49.6%">Processing</textPath></text></g>
    <g transform="rotate(180)"><use href="#arrow" class="fill-refine"/>
      <text class="seg-label"><textPath href="#ccw-inner" startOffset="50.4%">Refining</textPath></text>
      <text class="seg-label"><textPath href="#ccw-outer" startOffset="50.4%">Precious Metals</textPath></text></g>
    <g transform="rotate(240)"><use href="#arrow" class="fill-metal"/>
      <text class="seg-label"><textPath href="#cw-outer" startOffset="49.6%">Metal Products</textPath></text>
      <text class="seg-label"><textPath href="#cw-inner" startOffset="49.6%">Manufactured</textPath></text></g>
    <g transform="rotate(300)"><use href="#arrow" class="fill-return"/>
      <text class="seg-label"><textPath href="#cw-outer" startOffset="49.6%">Products Return</textPath></text>
      <text class="seg-label"><textPath href="#cw-inner" startOffset="49.6%">to OEMs</textPath></text></g>
    <text class="loop-title" y="-150">ELM</text>
    <text class="loop-title" y="-77">SUSTAINABILITY</text>
    <text class="loop-title" y="-5">&amp; RENEWABLE</text>
    <text class="loop-title" y="65">RESOURCE</text>
    <text class="loop-title" y="137">LOOP</text>
  </g>

  <!-- Ring C: flat chevrons -->
  <g class="loop loop-chevron" transform="translate(477 1470)">
    <g transform="rotate(0)"><use href="#arrow" class="fill-scrap"/>
      <text class="seg-label"><textPath href="#cw-outer" startOffset="49.6%">End-of-life Product</textPath></text>
      <text class="seg-label"><textPath href="#cw-inner" startOffset="49.6%">&amp; Mfg. Scrap</textPath></text></g>
    <g transform="rotate(60)"><use href="#arrow" class="fill-ubne"/>
      <text class="seg-label"><textPath href="#cw-mid" startOffset="49.6%">UBNE Services</textPath></text></g>
    <g transform="rotate(120)"><use href="#arrow" class="fill-mech"/>
      <text class="seg-label"><textPath href="#cw-outer" startOffset="49.6%">Mechanical</textPath></text>
      <text class="seg-label"><textPath href="#cw-inner" startOffset="49.6%">Processing</textPath></text></g>
    <g transform="rotate(180)"><use href="#arrow" class="fill-refine"/>
      <text class="seg-label"><textPath href="#ccw-inner" startOffset="50.4%">Refining</textPath></text>
      <text class="seg-label"><textPath href="#ccw-outer" startOffset="50.4%">Precious Metals</textPath></text></g>
    <g transform="rotate(240)"><use href="#arrow" class="fill-metal"/>
      <text class="seg-label"><textPath href="#cw-outer" startOffset="49.6%">Metal Products</textPath></text>
      <text class="seg-label"><textPath href="#cw-inner" startOffset="49.6%">Manufactured</textPath></text></g>
    <g transform="rotate(300)"><use href="#arrow" class="fill-return"/>
      <text class="seg-label"><textPath href="#cw-outer" startOffset="49.6%">Products Return</textPath></text>
      <text class="seg-label"><textPath href="#cw-inner" startOffset="49.6%">to OEMs</textPath></text></g>
    <text class="loop-title" y="-150">ELM</text>
    <text class="loop-title" y="-77">SUSTAINABILITY</text>
    <text class="loop-title" y="-5">&amp; RENEWABLE</text>
    <text class="loop-title" y="65">RESOURCE</text>
    <text class="loop-title" y="137">LOOP</text>
  </g>

  <!-- Ring D: two-tone chevrons -->
  <g class="loop loop-two-tone" transform="translate(1435 1475)">
    <g transform="rotate(0)"><use href="#arrow" class="fill-scrap"/><use href="#arrow" class="fill-scrap-lt" clip-path="url(#inner-band)"/>
      <text class="seg-label"><textPath href="#cw-outer" startOffset="49.6%">End-of-life Product</textPath></text>
      <text class="seg-label"><textPath href="#cw-inner" startOffset="49.6%">&amp; Mfg. Scrap</textPath></text></g>
    <g transform="rotate(60)"><use href="#arrow" class="fill-ubne"/><use href="#arrow" class="fill-ubne-lt" clip-path="url(#inner-band)"/>
      <text class="seg-label"><textPath href="#cw-mid" startOffset="49.6%">UBNE Services</textPath></text></g>
    <g transform="rotate(120)"><use href="#arrow" class="fill-mech"/><use href="#arrow" class="fill-mech-lt" clip-path="url(#inner-band)"/>
      <text class="seg-label"><textPath href="#cw-outer" startOffset="49.6%">Mechanical</textPath></text>
      <text class="seg-label"><textPath href="#cw-inner" startOffset="49.6%">Processing</textPath></text></g>
    <g transform="rotate(180)"><use href="#arrow" class="fill-refine"/><use href="#arrow" class="fill-refine-lt" clip-path="url(#inner-band)"/>
      <text class="seg-label"><textPath href="#ccw-inner" startOffset="50.4%">Refining</textPath></text>
      <text class="seg-label"><textPath href="#ccw-outer" startOffset="50.4%">Precious Metals</textPath></text></g>
    <g transform="rotate(240)"><use href="#arrow" class="fill-metal"/><use href="#arrow" class="fill-metal-lt" clip-path="url(#inner-band)"/>
      <text class="seg-label"><textPath href="#cw-outer" startOffset="49.6%">Metal Products</textPath></text>
      <text class="seg-label"><textPath href="#cw-inner" startOffset="49.6%">Manufactured</textPath></text></g>
    <g transform="rotate(300)"><use href="#arrow" class="fill-return"/><use href="#arrow" class="fill-return-lt" clip-path="url(#inner-band)"/>
      <text class="seg-label"><textPath href="#cw-outer" startOffset="49.6%">Products Return</textPath></text>
      <text class="seg-label"><textPath href="#cw-inner" startOffset="49.6%">to OEMs</textPath></text></g>
    <text class="loop-title" y="-150">ELM</text>
    <text class="loop-title" y="-77">SUSTAINABILITY</text>
    <text class="loop-title" y="-5">&amp; RENEWABLE</text>
    <text class="loop-title" y="65">RESOURCE</text>
    <text class="loop-title" y="137">LOOP</text>
  </g>
</svg>
</body>
</html>
```